Shampoo and Shower Gel Packaging Design

I need a new packaging design for a men shampoo and shower gel bottle. The packaging must me black (black bottle/package) and the logo should be also monochrom.
For example, black matte bottle and black shiny logo on the packaging (not mandatory).
the design must contain maximum 3 colors.
1. black
2. white (text)
3. grey/dark blue/dark green (colors will be the difference between products parfumes/smell/scences.

Design must be minimalist/elegant/discrete.
Updates

Please check the photos i added for pure inspiration.

Target Market(s)

brand exclusively for MEN - premium clients

Industry/Entity Type

Cosmetics

Font styles to use
Sans Serif

Colors
1b1b1b
5c5c5c
aaaaaa
ffffff
3176b5

Requirements
Must have
• black background
• minimalist design

```html
<!DOCTYPE html>
<html lang="en">
<head>
<meta charset="utf-8">
<title>NORVE Cosmetics – Bath &amp; Shower Gel Labels</title>
<link rel="stylesheet" href="https://fonts.googleapis.com/css2?family=Montserrat:wght@300&family=Arimo:wght@400&display=swap">
<style>
  :root {
    --page-bg: #ffffff;
    --label-black: #000000;
    --scent-aqua: #1fb6cf;
    --scent-lime: #4cff00;
    --scent-stone: #b4b9b9;
    --text-light: #ffffff;
    --ml-text: #1b1b1b;
  }

  * { margin: 0; padding: 0; box-sizing: border-box; }

  html, body {
    width: 730px;
    height: 1200px;
    overflow: hidden;
    background: var(--page-bg);
  }

  .sheet {
    position: relative;
    width: 730px;
    height: 1200px;
  }

  /* One label component, 208 × 402 */
  .label {
    position: absolute;
    width: 208px;
    height: 402px;
    background: var(--label-black);
    color: var(--accent);
    text-align: center;
    transform-origin: top left;
  }

  .label--aqua  { --accent: var(--scent-aqua); }
  .label--lime  { --accent: var(--scent-lime); }
  .label--stone { --accent: var(--scent-stone); }

  .label--hero  { left: 230px; top: 168px; transform: scale(1.3); }
  .label--left  { left: 34px;  top: 745px; }
  .label--mid   { left: 261px; top: 745px; }
  .label--right { left: 488px; top: 745px; }

  .brand {
    position: absolute;
    left: 0;
    right: 0;
    top: 40px;
    font-family: "Montserrat", sans-serif;
    font-weight: 300;
    color: var(--accent);
  }

  .brand__dot {
    display: block;
    width: 22px;
    height: 22px;
    margin: 0 auto 14px;
    border-radius: 50%;
    background: var(--accent);
  }

  .brand__name {
    display: block;
    font-size: 30px;
    line-height: 1;
    letter-spacing: 9px;
    padding-left: 9px;
  }

  .brand__sub {
    display: block;
    margin-top: 6px;
    font-size: 6.5px;
    letter-spacing: 3px;
    padding-left: 3px;
  }

  .product {
    position: absolute;
    left: 0;
    right: 0;
    top: 218px;
    font-family: "Arimo", sans-serif;
    color: var(--accent);
  }

  .product__name {
    font-size: 12px;
    letter-spacing: 1.6px;
  }

  .product__sub {
    margin-top: 18px;
    font-size: 7.5px;
    letter-spacing: 0.8px;
  }

  .volume {
    position: absolute;
    left: 20px;
    top: 276px;
    width: 168px;
    height: 94px;
  }

  .volume svg {
    display: block;
    width: 100%;
    height: 100%;
  }

  .volume__text {
    position: absolute;
    left: 0;
    right: 0;
    top: 52px;
    font-family: "Arimo", sans-serif;
    font-size: 7.5px;
    color: var(--ml-text);
  }
</style>
</head>
<body>
<main class="sheet">

  <section class="label label--aqua label--hero">
    <div class="brand"><span class="brand__dot"></span><span class="brand__name">NORVE</span><span class="brand__sub">COSMETICS</span></div>
    <div class="product"><p class="product__name">BATH &amp; SHOWER GEL</p><p class="product__sub">GEL BAIN DOUCHE MAN</p></div>
    <div class="volume"><svg viewBox="0 0 168 94" preserveAspectRatio="none"><polygon points="0,0 168,0 84,94" fill="var(--scent-aqua)"/></svg><p class="volume__text">200 ml</p></div>
  </section>

  <section class="label label--aqua label--left">
    <div class="brand"><span class="brand__dot"></span><span class="brand__name">NORVE</span><span class="brand__sub">COSMETICS</span></div>
    <div class="product"><p class="product__name">BATH &amp; SHOWER GEL</p><p class="product__sub">GEL BAIN DOUCHE MAN</p></div>
    <div class="volume"><svg viewBox="0 0 168 94" preserveAspectRatio="none"><polygon points="0,0 168,0 84,94" fill="var(--scent-aqua)"/></svg><p class="volume__text">200 ml</p></div>
  </section>

  <section class="label label--lime label--mid">
    <div class="brand"><span class="brand__dot"></span><span class="brand__name">NORVE</span><span class="brand__sub">COSMETICS</span></div>
    <div class="product"><p class="product__name">BATH &amp; SHOWER GEL</p><p class="product__sub">GEL BAIN DOUCHE MAN</p></div>
    <div class="volume"><svg viewBox="0 0 168 94" preserveAspectRatio="none"><polygon points="0,0 168,0 84,94" fill="var(--scent-lime)"/></svg><p class="volume__text">200 ml</p></div>
  </section>

  <section class="label label--stone label--right">
    <div class="brand"><span class="brand__dot"></span><span class="brand__name">NORVE</span><span class="brand__sub">COSMETICS</span></div>
    <div class="product"><p class="product__name">BATH &amp; SHOWER GEL</p><p class="product__sub">GEL BAIN DOUCHE MAN</p></div>
    <div class="volume"><svg viewBox="0 0 168 94" preserveAspectRatio="none"><polygon points="0,0 168,0 84,94" fill="var(--scent-stone)"/></svg><p class="volume__text">200 ml</p></div>
  </section>

</main>
</body>
</html>
```